Dune Air & Plus business card

I need an awesome, double-sided business card designed with our new logo. I would like the one side black with the colored logo, and the back side is all yours. I'd like to see horizontal and vertical layouts. Get creative! Thank you.

Target Market(s)

HVAC, Heating and Cooling in Phoenix, AZ

Industry/Entity Type

HVAC

Contact Information for Business Card

We need our new logo on the card. Tom Harker, (623) 555-0142, tom@trydunesair.com, www.trydunesair.com, ROC 514273

```html
<!DOCTYPE html>
<html lang="en">
<head>
<meta charset="utf-8">
<title>Dune Air &amp; Plus – Business Card</title>
<link rel="stylesheet" href="https://fonts.googleapis.com/css2?family=Roboto+Slab:wght@300;400;700&display=swap">
<style>
  :root {
    --page-bg: #e9e9e4;
    --card-front: #000000;
    --card-back: #ffffff;
    --brand-blue: #1172c0;
    --brand-orange: #f0862a;
    --text-dark: #3a3a3a;
    --text-light: #ffffff;
  }
  * { margin: 0; padding: 0; box-sizing: border-box; }
  html, body {
    width: 1200px; height: 1200px; overflow: hidden;
    background: var(--page-bg);
    font-family: "Roboto Slab", Georgia, serif;
  }
  .card {
    position: absolute;
    left: 231px;
    width: 737px; height: 420px;
    border-radius: 4px;
    overflow: hidden;
    box-shadow: 0 6px 18px rgba(0,0,0,0.18);
  }
  .card--front { top: 155px; background: var(--card-front); }
  .card--back  { top: 637px; background: var(--card-back); }

  .brand-name {
    position: absolute;
    display: flex; align-items: center; gap: 12px;
    transform: translate(-50%, -50%);
    white-space: nowrap;
  }
  .brand-name__dot {
    width: 18px; height: 18px; border-radius: 50%;
    background: var(--brand-orange);
  }
  .brand-name__text {
    font-weight: 700;
    color: var(--brand-blue);
  }
  .card--front .brand-name { left: 344px; top: 227px; }
  .card--front .brand-name__text { font-size: 38px; }
  .card--back .brand-name { left: 140px; top: 208px; }
  .card--back .brand-name__text { font-size: 24px; }
  .card--back .brand-name__dot { width: 14px; height: 14px; }

  .name-band {
    position: absolute; top: 42px; right: 0;
    width: 420px; height: 73px;
    background: var(--brand-blue);
    clip-path: polygon(0 0, 100% 0, 100% 100%, 51px 100%);
  }
  .holder {
    position: absolute; left: 438px; top: 58px;
    color: var(--text-light);
  }
  .holder__name { font-size: 24px; font-weight: 700; line-height: 1; letter-spacing: -0.3px; }
  .holder__title { font-size: 18px; font-weight: 300; line-height: 1.3; margin-top: 2px; }

  .contact-list { list-style: none; }
  .contact-item {
    position: absolute; left: 316px;
    display: flex; align-items: center; gap: 9px;
    transform: translateY(-50%);
    font-size: 18px; font-weight: 300; color: var(--text-dark);
  }
  .contact-item__icon {
    width: 40px; height: 40px; border-radius: 50%;
    background: var(--brand-blue);
    display: flex; align-items: center; justify-content: center;
    flex-shrink: 0;
  }
  .contact-item__icon svg { width: 20px; height: 20px; }
  .contact-item--phone { top: 181px; }
  .contact-item--licence { top: 243px; }
  .contact-item--email { top: 298px; }
  .contact-item--web { top: 358px; }
</style>
</head>
<body>
  <section class="card card--front">
    <div class="brand-name">
      <span class="brand-name__dot"></span>
      <span class="brand-name__text">Dune Air &amp; Plus</span>
    </div>
  </section>

  <section class="card card--back">
    <div class="brand-name">
      <span class="brand-name__dot"></span>
      <span class="brand-name__text">Dune Air &amp; Plus</span>
    </div>

    <div class="name-band"></div>
    <div class="holder">
      <p class="holder__name">Tom Harker</p>
      <p class="holder__title">Chief Executive Manager</p>
    </div>

    <ul class="contact-list">
      <li class="contact-item contact-item--phone">
        <span class="contact-item__icon">
          <svg viewBox="0 0 24 24" fill="#fff"><path d="M3 9c0-3 4-4 9-4s9 1 9 4v2h-4V9H7v2H3z"/><path d="M6 12h12l2 8H4z"/><circle cx="12" cy="16" r="2.2" fill="#1172c0"/></svg>
        </span>
        <span>(623) 555-0142</span>
      </li>
      <li class="contact-item contact-item--licence">
        <span class="contact-item__icon">
          <svg viewBox="0 0 24 24" fill="#fff"><path d="M12 2a7 7 0 0 0-7 7c0 5 7 13 7 13s7-8 7-13a7 7 0 0 0-7-7z"/><circle cx="12" cy="9" r="2.6" fill="#1172c0"/></svg>
        </span>
        <span>ROC 514273</span>
      </li>
      <li class="contact-item contact-item--email">
        <span class="contact-item__icon">
          <svg viewBox="0 0 24 24" fill="#fff"><path d="M2 4l20 8-20 8 4-8z"/><path d="M6 12h8" stroke="#1172c0" stroke-width="1.5"/></svg>
        </span>
        <span>tom@trydunesair.com</span>
      </li>
      <li class="contact-item contact-item--web">
        <span class="contact-item__icon">
          <svg viewBox="0 0 24 24" fill="none" stroke="#fff" stroke-width="1.8"><circle cx="12" cy="12" r="9"/><ellipse cx="12" cy="12" rx="4" ry="9"/><path d="M3 12h18"/></svg>
        </span>
        <span>www.trydunesair.com</span>
      </li>
    </ul>
  </section>
</body>
</html>
```